Eye-catching & Glamorous Labels for Skincare Bottles & Jars

We need new labels designed for our product range as we have been dormant for a few years and are now rebranding Tindra Mist - Cruelty Free Skincare. The label sizes are defined in the attached word document. All products have either a bright silver or a matte silver lid pump/spray so please keep this in mind.

We are open to colours and invite you to create bright trendy labels which are coordinated with the logo attached. The logo is not of any specific colour so dark on light, light on dark, tone on tone - we like purple / duck egg blue / turquoise WITH matte silver, however stronger colours like navy plus maroon with matte silver is also a strong favourite. If you feel inspired by a colour you think would be appropriate to Tindra Mist please feel free to have a go.

A front section for product information is required and the back should include relevant details ie ingredients, company info, and a note that there has been no testing on animals.

The serum bottle will require a front and back label on a clear label in a pale colour to coordinate with the rest of the range. Size for this label is 35mm top edge, 25mm bottom edge, height 45mm - I have attached a picture of the serum bottle as they were originally pad printed. Please don't hesitate to contact me for any further information. Good luck!

Target Market(s)

Educated professional women 30-45 who are regular skincare users and looking for beautiful skincare products without animal derived ingredients and animal testing

Industry/Entity Type

Skin Care Product

Font styles to use
Serif
Sans Serif
Decorative
Script

Colors

Designer to choose colors to be used in the design.

Requirements
Must have
• Tindra Mist Logo - eye catching design - not too busy or cramped.
Nice to have
• Is it possible to create a background pattern using a very small image of the logo? Just a thought.

```html
<!DOCTYPE html>
<html lang="en">
<head>
<meta charset="utf-8">
<title>Tindra Mist – Day Cream Label</title>
<link rel="stylesheet" href="https://fonts.googleapis.com/css2?family=Didact+Gothic&display=swap">
<style>
  :root {
    --page-bg: #f6f6f6;
    --label-deep: #63005e;
    --label-mid: #720070;
    --label-light: #6c006a;
    --ink: #f1eef2;
    --ink-soft: #e6dfe8;
  }
  html, body {
    margin: 0;
    padding: 0;
    width: 900px;
    height: 1200px;
    overflow: hidden;
    background: var(--page-bg);
  }
  .canvas {
    position: relative;
    width: 900px;
    height: 1200px;
    background: var(--page-bg);
    font-family: "Didact Gothic", "Century Gothic", sans-serif;
  }
  .label-shape {
    position: absolute;
    left: 0;
    top: 0;
  }
  .label-text {
    position: absolute;
    left: 130px;
    width: 640px;
    text-align: center;
    color: var(--ink);
    margin: 0;
    font-weight: 400;
  }
  .brand-name {
    top: 300px;
    font-size: 58px;
    letter-spacing: 1px;
    line-height: 1;
  }
  .brand-tagline {
    top: 430px;
    font-size: 25px;
    color: var(--ink-soft);
  }
  .product-name {
    top: 625px;
    font-size: 54px;
    line-height: 1;
  }
  .product-claim {
    top: 708px;
    font-size: 25px;
    color: var(--ink-soft);
  }
  .product-volume {
    top: 835px;
    font-size: 23px;
    color: var(--ink-soft);
  }
</style>
</head>
<body>
  <main class="canvas">
    <svg class="label-shape" width="900" height="1200" viewBox="0 0 900 1200" aria-hidden="true">
      <defs>
        <linearGradient id="labelFill" x1="0" y1="0" x2="1" y2="0">
          <stop offset="0" stop-color="var(--label-deep)"/>
          <stop offset="0.5" stop-color="var(--label-mid)"/>
          <stop offset="1" stop-color="var(--label-light)"/>
        </linearGradient>
      </defs>
      <path d="M130,182 Q130,166 146,163 Q450,100 754,163 Q770,166 770,182 L770,1028 Q770,1044 754,1047 Q450,1110 146,1047 Q130,1044 130,1028 Z" fill="url(#labelFill)"/>
    </svg>

    <h1 class="label-text brand-name">Tindra Mist</h1>
    <p class="label-text brand-tagline">Cruelty Free Skin Care</p>
    <h2 class="label-text product-name">Day Cream</h2>
    <p class="label-text product-claim">Anti aging Technology</p>
    <p class="label-text product-volume">100 ml</p>
  </main>
</body>
</html>
```